KV Group

We need a new website for our company and since we had a very good work done for our logo in this site, we're back for the entire job.

Our company name is Marlowe Capital Group. We're adding files of examples of what we have done today. In my opinion we need a more attention lock in the site but yet financial simple work.

Our files (attached) will let you know what we have so far. We need a complete change but the colours should be the same, however you can change them not running away to far from the original, and of course matching with the logo.

We need examples for 3 kind of layouts.

- A HOME welcome layout
- An internal Layout with sidebar
- And internal Layout wide

We can buy image licenses if needed for assets.
Actually there are 5 slide images placed on the Welcome HOME, we need those there, but you can improve with better images to match the new website!!!

Target Market(s)

Clients looking for financial advisers, tax and funds specialist, currency advisers

Industry/Entity Type

Financial

Requirements
Must have
• all the fonts must be in accordance with the financial market sites........the welcome home page must be precise, neat and information accurate........the menu should be elegant........main focus on the Home page, should be also the PRIVATE ACCESS box log in.......

```html
<!DOCTYPE html>
<html lang="en">
<head>
<meta charset="utf-8">
<title>Marlowe Capital Group</title>
<link href="https://fonts.googleapis.com/css2?family=Open+Sans:wght@300;400;600;700&family=PT+Sans:wght@400;700&family=PT+Serif:wght@400;700&display=swap" rel="stylesheet">
<style>
:root{
  --orange:#e8731f;
  --orange-light:#f08a2c;
  --orange-deep:#d8611a;
  --dark:#2b2b2b;
  --darker:#232323;
  --panel:#2f2f2f;
  --grey-text:#c9c9c9;
  --muted:#8a8a8a;
  --white:#ffffff;
  --navy:#1b2a6b;
  --green:#1e9a2a;
  --red:#d8261c;
}
*{margin:0;padding:0;box-sizing:border-box}
html,body{width:1200px;height:2333px;overflow:hidden}
body{position:relative;background:var(--white);font-family:"Open Sans",Arial,sans-serif;color:#333}
.abs{position:absolute}

/* header */
.brand{left:97px;top:40px;display:flex;align-items:center;gap:12px}
.brand-square{width:44px;height:44px;background:var(--orange)}
.brand-name{font-family:"Open Sans",sans-serif;font-weight:600;font-size:24px;color:#222;letter-spacing:.5px;white-space:nowrap}
.cta{top:15px;height:35px;background:linear-gradient(var(--orange-light),var(--orange-deep));border:1px solid #c85a14;border-radius:3px;color:#fff;font-family:"PT Serif",Georgia,serif;font-size:16px;font-weight:700;display:flex;align-items:center;justify-content:center;gap:9px;padding:0 8px;white-space:nowrap}
.cta svg{flex:none}
.cta-apply{left:805px;width:140px}
.cta-contact{left:955px;width:147px}
.main-nav{top:93px;left:540px;display:flex;font-size:14px;color:#111}
.main-nav a{position:absolute;top:0;height:24px;line-height:24px;color:#111;text-decoration:none;white-space:nowrap;transform:translateX(-50%)}
.main-nav a.active{background:var(--orange);color:#fff;padding:0 12px}
.dropdown{left:695px;top:120px;width:252px;height:257px;background:#3a3a3a;padding:4px 6px}
.dropdown li{list-style:none;height:27px;line-height:26px;border-bottom:1px solid #555;color:#fff;font-size:12.5px;padding-left:6px;white-space:nowrap}
.dropdown li::before{content:"›";margin-right:6px;color:#ddd}

/* hero band */
.orange-band{left:0;top:213px;width:1200px;height:762px;background:var(--orange)}
.slider{left:97px;top:150px;width:1006px;height:442px;background:linear-gradient(100deg,#d9dde2 0%,#8b8f98 35%,#cfd3d8 60%,#6a5a55 100%);box-shadow:0 20px 30px rgba(0,0,0,.25)}
.slider-caption{left:97px;top:480px;width:1006px;height:112px;background:rgba(30,30,30,.85);padding:10px 26px}
.slider-caption h2{font-weight:300;font-size:40px;color:var(--orange-light);line-height:44px;white-space:nowrap}
.slider-caption p{font-size:19px;color:#fff;line-height:24px}
.slide-arrow{top:342px;width:50px;height:50px;border-radius:50%;background:rgba(40,40,40,.85);border:2px solid #ddd}
.slide-arrow svg{display:block}

/* welcome */
.welcome-title{left:132px;top:668px;font-weight:400;font-size:36px;color:#fff;white-space:nowrap}
.welcome-text{left:137px;width:610px;font-size:12.5px;line-height:19px;color:#fff}
.welcome-photo{left:568px;top:803px;width:180px;height:112px;background:linear-gradient(#e4ecf2,#6f7d8c)}
.welcome-divider{left:777px;top:690px;width:1px;height:230px;background:rgba(255,255,255,.35)}
.login{left:805px;top:675px;width:262px;height:245px;background:#fff;border:2px solid #3a3a3a;box-shadow:0 4px 10px rgba(0,0,0,.3)}
.login-head{height:42px;background:#333;color:var(--orange-light);font-family:"PT Serif",serif;font-size:21px;line-height:42px;padding-left:20px}
.login-field{position:absolute;left:16px;width:222px;height:31px;border:1px solid #bbb;background:linear-gradient(#eee,#fff);font-family:"PT Serif",serif;font-size:13px;line-height:29px;padding-left:10px;color:#444}
.login-forgot{position:absolute;left:18px;top:160px;font-family:"PT Serif",serif;font-size:13px;color:#333;line-height:20px;white-space:nowrap}
.login-forgot span{color:var(--orange);text-decoration:underline}
.login-btn{position:absolute;left:100px;top:196px;width:138px;height:30px;background:linear-gradient(var(--orange-light),var(--orange-deep));color:#fff;font-family:"PT Serif",serif;font-size:14px;text-align:center;line-height:30px;border-radius:2px;white-space:nowrap}

/* services */
.band-edge{left:0;top:975px;width:1200px;height:5px;background:#f5a24f}
.service{top:1012px;width:304px;height:360px;background:var(--panel);border:1px solid #222;text-align:center;display:flex;flex-direction:column;align-items:center;padding-bottom:14px}
.service h3{font-weight:400;font-size:24px;color:var(--orange-light);margin-top:8px;height:40px;white-space:nowrap}
.service-photo{width:288px;height:143px;flex:none}
.service p{color:#fff;font-family:"PT Sans",Arial,sans-serif;font-weight:700;font-size:15px;line-height:19px;padding:12px 16px 0}
.read-more{margin-top:auto;width:118px;height:35px;line-height:33px;background:linear-gradient(#fff,#cfcfcf);border:1px solid #888;border-radius:3px;font-size:16px;color:#222;white-space:nowrap}

/* partners */
.partners{left:0;top:1413px;width:1200px;height:425px;background:var(--orange)}
.partners h2{position:absolute;top:42px;width:100%;text-align:center;font-weight:300;font-size:46px;color:#fff}
.badge{top:1541px;width:144px;height:144px;border-radius:50%;background:#fff;box-shadow:0 3px 6px rgba(0,0,0,.2)}
.badge i{position:absolute;left:30px;top:52px;width:84px;height:40px;border-radius:8px}
.ticker{left:97px;top:1735px;width:1006px;height:48px;background:#fff;display:flex;align-items:center;justify-content:center;gap:30px;font-weight:700;font-size:13px;color:var(--navy);white-space:nowrap;box-shadow:0 12px 14px -8px rgba(0,0,0,.35)}
.up{color:var(--green)}.down{color:var(--red)}.flat{color:var(--orange)}

/* footer */
.footer{left:0;top:1838px;width:1200px;height:316px;background:var(--dark);border-top:5px solid var(--orange-light)}
.fcol{top:1885px}
.fcol h4{font-weight:600;font-size:15px;color:var(--orange-light);margin-bottom:9px;white-space:nowrap}
.fcol li{list-style:none;font-size:13px;color:var(--grey-text);line-height:21px;white-space:nowrap}
.footer-note{left:0;top:2138px;width:1200px;height:154px;background:#333;padding:20px 150px;text-align:center;font-size:12px;line-height:19px;color:var(--muted)}
.footer-note em{color:var(--orange);font-weight:700}
.footer-note p+p{margin-top:19px}
.copyright{left:0;top:2292px;width:1200px;height:41px;background:var(--darker);text-align:center;line-height:41px;font-size:11.5px;color:var(--muted)}
</style>
</head>
<body>

<header>
  <div class="abs brand"><span class="brand-square"></span><span class="brand-name">Marlowe Capital Group</span></div>
  <a class="abs cta cta-apply">
    <svg width="20" height="20" viewBox="0 0 22 22"><rect x="1" y="4" width="16" height="16" fill="none" stroke="#fff" stroke-width="2"/><path d="M8 14l10-10 3 3-10 10H8z" fill="#fff"/></svg>Apply Now</a>
  <a class="abs cta cta-contact">
    <svg width="22" height="16" viewBox="0 0 24 18"><rect x="1" y="1" width="22" height="16" fill="none" stroke="#fff" stroke-width="2"/><path d="M1 1l11 9 11-9" fill="none" stroke="#fff" stroke-width="2"/></svg>Contact Us</a>
  <nav class="abs main-nav">
    <a style="left:35px">Home</a>
    <a style="left:112px">About Us</a>
    <a class="active" style="left:205px">Investments</a>
    <a style="left:287px">Funds</a>
    <a style="left:363px">Brokerage</a>
    <a style="left:452px">Exchange</a>
    <a style="left:535px">Accounts</a>
  </nav>
</header>

<div class="abs orange-band"></div>

<section>
  <div class="abs slider" role="img" aria-label="Team of smiling private bankers in a bright office"></div>
  <div class="abs slider-caption">
    <h2>TEAMWORK FOR YOUR BENIFIT</h2>
    <p>Our dedicated Private Bankers, will proactively keep you up to date with relevant information and provide a financial overview that enables you to make better decisions.</p>
  </div>
  <div class="abs slide-arrow" style="left:118px"><svg width="46" height="46"><path d="M27 13l-10 10 10 10" fill="none" stroke="#fff" stroke-width="4"/></svg></div>
  <div class="abs slide-arrow" style="left:1033px"><svg width="46" height="46"><path d="M19 13l10 10-10 10" fill="none" stroke="#fff" stroke-width="4"/></svg></div>
</section>

<ul class="abs dropdown">
  <li>Term Deposits</li><li>Management &amp; Strategy</li><li>Client Relations</li><li>Financial Privacy</li><li>Tax Advice</li><li>Wealth Analysis &amp; Financial Planning</li><li>Active Advisory Group</li><li>Manager Selection Services</li><li>Private Equity</li>
</ul>

<section>
  <h1 class="abs welcome-title">WELCOME TO OUR WEBSITE</h1>
  <p class="abs welcome-text" style="top:723px">Lorem ipsum dolor sit amet, consectetur adipiscing elit. Nulla lobortis consequat mauris, eget eleifend nunc viverra viverra. Ut ac risus odio. Aliquam pretium purus sed nulla feugiat blandit. Cras vel libero ut lacus eleifend tempor. Phasellus eleifend, magna non tincidunt accumsan, justo arcu cursus ipsum, non</p>
  <p class="abs welcome-text" style="top:800px;width:420px">Lorem ipsum dolor sit amet, consectetur adipiscing elit. Nulla lobortis consequat mauris, eget eleifend nunc viverra viverra. Ut ac risus odio. Aliquam pretium purus sed nulla feugiat blandit. Cras vel libero ut lacus eleifend tempor. Phasellus eleifend, magna non tincidunt accumsan, justo arcu cursus ipsum, non porttitor sapien quam vel magna. Maecenas elit nisl, molestie nec dapibus nec,</p>
  <div class="abs welcome-photo" role="img" aria-label="Business colleagues meeting around a table"></div>
  <div class="abs welcome-divider"></div>

  <form class="abs login">
    <div class="login-head">Private Access</div>
    <div class="login-field" style="top:65px">Acc. Number</div>
    <div class="login-field" style="top:110px">Acc. Password</div>
    <p class="login-forgot">Forgot Your Acc. Number/Password?<br><span>Click Here!</span></p>
    <div class="login-btn">Log In to Account</div>
  </form>
</section>

<div class="abs band-edge"></div>

<section>
  <article class="abs service" style="left:133px">
    <h3>Management &amp; Strategy</h3>
    <div class="service-photo" role="img" aria-label="Advisers meeting in a glass office" style="background:linear-gradient(#e9eef2,#7c8791)"></div>
    <p>Lorem ipsum dolor sit amet, consectetur adipiscing elit. Nulla lobortis consequat mauris, eget eleifend nunc viverra viverra. Ut ac risus odio. Aliquam pretium purus sed nulla feugiat blandit. Cras vel</p>
    <span class="read-more">Read More</span>
  </article>
  <article class="abs service" style="left:448px">
    <h3>Funds</h3>
    <div class="service-photo" role="img" aria-label="Hand signing documents on a desk" style="background:linear-gradient(#f4f2ee,#b9b2a7)"></div>
    <p>Lorem ipsum dolor sit amet, consectetur adipiscing elit. Nulla lobortis consequat mauris, eget eleifend nunc viverra viverra. Ut ac risus odio. Aliquam pretium purus sed nulla feugiat blandit. Cras vel</p>
    <span class="read-more">Read More</span>
  </article>
  <article class="abs service" style="left:762px">
    <h3>Currency Exchange</h3>
    <div class="service-photo" role="img" aria-label="Calculator and pen on a financial chart" style="background:linear-gradient(120deg,#6e6f74,#d9dadf 60%,#8a5b5b)"></div>
    <p>Lorem ipsum dolor sit amet, consectetur adipiscing elit. Nulla lobortis consequat mauris, eget eleifend nunc viverra viverra. Ut ac risus odio. Aliquam pretium purus sed nulla feugiat blandit. Cras vel</p>
    <span class="read-more">Read More</span>
  </article>
</section>

<section class="abs partners"><h2>VARIFIED AND POWERED BY</h2></section>
<div class="abs badge" style="left:275px"><i style="background:#c9c9c9"></i></div>
<div class="abs badge" style="left:446px"><i style="background:#2b4fa8"></i></div>
<div class="abs badge" style="left:615px"><i style="background:#7cb342"></i></div>
<div class="abs badge" style="left:785px;border:8px solid var(--orange-deep)"><i style="left:22px;top:44px;background:#1d3f8f;border-radius:50%;width:84px;height:40px"></i></div>

<div class="abs ticker">
  <span>GBP/UAH= <span class="up">12.65761 ▲</span></span>
  <span>GBP/UGX= <span class="down">4010.06174 ▼</span></span>
  <span>GBP/USD= <span class="up">1.55817 ▲</span></span>
  <span>GBP/UYU= <span class="up">35.36026 ▲</span></span>
  <span>GBP/VEF= <span class="flat">0</span></span>
  <span>GBP/VUV= <span class="up">151.6953 ▲</span></span>
</div>

<footer>
  <div class="abs footer"></div>
  <div class="abs fcol" style="left:152px"><h4>About Us</h4><ul><li>History</li><li>Expertize</li><li>Identity</li><li>Strategy</li><li>Contact Us</li></ul></div>
  <div class="abs fcol" style="left:298px"><h4>Investments</h4><ul><li>Term Deposits</li><li>Management &amp; Strategy</li><li>Client Relations</li><li>Financial Privacy</li><li>Tax Advice</li><li>Wealth Analysis &amp; Financial Planning</li><li>Active Advisory Group</li><li>Manager Selection Services</li><li>Private Equity</li></ul></div>
  <div class="abs fcol" style="left:568px"><h4>Funds</h4><ul><li>Overview</li><li>Administration</li><li>Funds Security</li><li>Core Services</li><li>Reporting</li><li>Revenue Opportunities</li><li>How it works?</li><li>Glossary</li></ul></div>
  <div class="abs fcol" style="left:772px"><h4>Currency Exchange</h4><ul><li>Foreign Exchange</li><li>Fx Forword</li><li>Fx Options</li></ul></div>
  <div class="abs fcol" style="left:772px;top:2018px"><h4>Accounts</h4><ul><li>Apply Now</li><li>Private Access</li></ul></div>
  <div class="abs fcol" style="left:978px"><h4>Brokerage</h4><ul><li>institutional</li><li>Research</li><li>Trading</li></ul></div>

  <div class="abs footer-note">
    <p>Lorem ipsum dolor sit amet, consectetur adipiscing elit. Nulla lobortis consequat mauris, eget eleifend nunc viverra viverra. Ut ac risus odio. Aliquam pretium purus sed nulla feugiat blandit. <em>Cras vel libero ut lacus</em> eleifend tempor. Phasellus eleifend, magna non tincidunt accumsan, justo arcu cursus ipsum,</p>
    <p>Maecenas elit nisl, molestie nec dapibus nec, aliquet a erat. Donec scelerisque lacus a <em>libero suscipit auctor volutpat</em> enim euismod. Lorem ipsum dolor sit amet, consectetur adipiscing elit. Nulla lobortis consequat mauris, eget eleifend nunc viverra viverra. Ut ac risus odio. Aliquam pretium purus sed nulla feugiat blandit. Cras vel libero ut lacus eleifend tempor. Phasellus eleifend, magna non tincidunt accumsan, justo arcu cursus ipsum,</p>
  </div>
  <div class="abs copyright">© 2013 Marlowe Capital Group,&nbsp;&nbsp; All rights reserved.</div>
</footer>

</body>
</html>
```